New business card design to go with our new logo

just want an eye-catching business card to go with our new logo. We are open to double sided or single sided. Just want it to have the following info on it. Whatever layout you think looks best.

First and Last Name
Title
Phone 801-555-0187
Address 312 W. Larkmoor Avenue Orem UT 84057
Email thecrew@meadowstailandkennel.example

Industry/Entity Type

Business

```html
<!DOCTYPE html>
<html lang="en">
<head>
<meta charset="utf-8">
<title>Meadows Tail &amp; Kennel – Business Card</title>
<link rel="stylesheet" href="https://fonts.googleapis.com/css2?family=Quicksand:wght@500;600;700&display=swap">
<style>
  :root {
    --page: #e9ecef;
    --card: #fbfbfa;
    --blue: #2196d3;
    --orange: #ee8a3d;
    --orange-soft: #f8c9a2;
    --paw-tint: #eef1f4;
  }
  * { margin: 0; padding: 0; box-sizing: border-box; }
  html, body { width: 1200px; height: 773px; overflow: hidden; }
  body {
    background: var(--page);
    font-family: "Quicksand", sans-serif;
    display: flex;
    align-items: center;
    justify-content: center;
  }
  .business-card {
    position: relative;
    width: 1080px;
    height: 617px;
    background: var(--card);
    box-shadow: 0 10px 30px rgba(0, 0, 0, 0.12);
    overflow: hidden;
  }
  .paw-pattern {
    position: absolute;
    left: 0;
    top: 200px;
    width: 560px;
    height: 417px;
    background: radial-gradient(ellipse at 30% 50%, var(--paw-tint) 0%, rgba(238,241,244,0) 70%);
  }
  .contact-block {
    position: absolute;
    right: 540px;
    top: 140px;
    text-align: right;
    color: var(--blue);
    font-weight: 700;
    font-size: 25px;
    line-height: 1.3;
  }
  .contact-phone { margin-bottom: 26px; }
  .contact-address { margin-bottom: 28px; }
  .contact-email { font-size: 23px; white-space: nowrap; }
  .person {
    position: absolute;
    right: 540px;
    top: 370px;
    text-align: right;
  }
  .person-name {
    font-size: 56px;
    font-weight: 700;
    color: var(--orange-soft);
    -webkit-text-stroke: 1.5px var(--orange);
    letter-spacing: 1px;
    white-space: nowrap;
  }
  .person-title {
    font-size: 32px;
    font-weight: 700;
    color: var(--orange);
    margin-top: 4px;
  }
  .brand {
    position: absolute;
    left: 600px;
    width: 390px;
    top: 140px;
    display: flex;
    flex-direction: column;
    align-items: center;
  }
  .brand-mark {
    width: 200px;
    height: 200px;
    border-radius: 50%;
    background: var(--blue);
  }
  .brand-name {
    margin-top: 34px;
    text-align: center;
    color: var(--orange);
    font-weight: 700;
    font-size: 50px;
    line-height: 1.05;
  }
</style>
</head>
<body>
  <div class="business-card">
    <div class="paw-pattern" role="img" aria-label="Faint pale paw-print pattern"></div>

    <div class="contact-block">
      <p class="contact-phone">801-555-0187</p>
      <p class="contact-address">312 W. Larkmoor Avenue<br>Orem UT 84057</p>
      <p class="contact-email">thecrew@meadowstailandkennel.example</p>
    </div>

    <div class="person">
      <p class="person-name">Dana Whitfield</p>
      <p class="person-title">- CEO</p>
    </div>

    <div class="brand">
      <div class="brand-mark" aria-hidden="true"></div>
      <p class="brand-name">Meadows<br>Tail &amp; Kennel</p>
    </div>
  </div>
</body>
</html>
```